New Newspaper Ad Design Project

We need an ad design for a magazine to promote our online courses. We're a beverage digital newspaper and recently we launched a platform dedicated to tasting courses. Now we want to promote them on a magazine.
The ad must be visually coherent with the website www.bottegamalto.it
Attached is a zip file with an image and a graphic pattern.
The headline is "Corsi online sulla birra"
A second text is the following
La proposta didattica di Bottega malto:
- Corso di degustazione
- Master sulle birre acide
- Master sugli abbinamenti
- Master sulle birre luppolate
- Focus mensili sul movimento italiano
- Esercitazioni pratiche di assaggio
A third text is the following (presented like a claim or tagline):
Con le birre in assaggio spedite direttamente a casa
We also need to promote a coupon with this text:
Usa il coupon VELANTRA10 per uno sconto di € 10 sul carrello*
(small text) * Coupon valido per tutto il 2022
Attached is another zip file with platform logo (2 versions) named "Logo Bottega Malto", that we expect big in the page
Our magazine logo is inside a third zip file named "Logo per media" (several versions). We expect it in the lowest part of the page with this text:
Una garanzia
Diario del Calice
(Diario del Calice is the text inside the logo).
The ad design must be a mix of images and texts. A4 size (21 x 29,7 cm) with +0,5 cm of bleed area or, if you prefer, a graphic grid of 18 x 26,4 cm.
We need a source file in PSD format.
Target Market(s)
Beer enthusiasts
Industry/Entity Type
Beer
Other font styles liked:
- Roboto Slab

```html
<!DOCTYPE html>
<html lang="it">
<head>
<meta charset="utf-8">
<title>Bottega Malto – Corsi online sulla birra</title>
<link href="https://fonts.googleapis.com/css2?family=Alfa+Slab+One&family=Roboto+Slab:wght@300;400;600;700&display=swap" rel="stylesheet">
<style>
  :root {
    --page-bg: #dcdcdc;
    --brown-deep: #2a1506;
    --brown-warm: #6b4323;
    --red: #e0331d;
    --red-deep: #d1281a;
    --orange: #f47a1d;
    --amber: #f9a51b;
    --gold: #f4b323;
    --cream: #fff4dd;
    --white: #ffffff;
    --grey-text: #5a5a5a;
  }
  * { margin: 0; padding: 0; box-sizing: border-box; }
  html, body { width: 1200px; height: 2169px; overflow: hidden; background: var(--page-bg); }
  body { position: relative; font-family: "Roboto Slab", serif; }

  .ad {
    position: absolute; left: 0; top: 236px;
    width: 1200px; height: 1697px; overflow: hidden; background: var(--white);
  }
  .ad-shapes { position: absolute; inset: 0; }

  .photo-area {
    position: absolute; left: 0; top: 0; width: 1200px; height: 900px;
    background:
      radial-gradient(ellipse at 78% 40%, #b98a5c 0%, #7a5232 35%, transparent 70%),
      linear-gradient(90deg, var(--brown-deep) 0%, #3a1f0b 40%, var(--brown-warm) 100%);
  }

  .brand {
    position: absolute; left: 96px; top: 92px;
    display: flex; align-items: center; gap: 18px;
  }
  .brand-square { width: 50px; height: 50px; background: var(--gold); }
  .brand-name {
    font-family: "Roboto Slab", serif; font-weight: 600; font-size: 66px;
    color: var(--gold); line-height: 1; letter-spacing: 1px;
  }

  .headline { position: absolute; left: 92px; top: 250px; color: var(--white); }
  .headline-line { display: flex; align-items: baseline; gap: 14px; line-height: 1; }
  .headline-line + .headline-line { margin-top: 10px; }
  .headline-strong {
    font-family: "Alfa Slab One", serif; font-size: 112px; line-height: 1;
  }
  .headline-strong.red { color: var(--red); -webkit-text-stroke: 3px var(--white); }
  .headline-strong.gold { color: var(--gold); -webkit-text-stroke: 3px var(--white); }
  .headline-light { font-weight: 300; font-size: 70px; }

  .tagline-badge {
    position: absolute; left: 727px; top: 706px; width: 380px; height: 380px;
    display: flex; flex-direction: column; align-items: center; justify-content: center;
    text-align: center; line-height: 1.12; font-size: 42px;
  }
  .tagline-badge .light { font-weight: 400; color: var(--grey-text); }
  .tagline-badge .gold { font-weight: 700; color: var(--gold); }
  .tagline-badge .grey { font-weight: 700; color: var(--grey-text); }
  .tagline-badge .red { font-weight: 700; color: var(--red); }

  .offer-title {
    position: absolute; left: 86px; top: 880px;
    font-weight: 700; font-size: 72px; line-height: 78px; color: var(--white);
  }

  .course-list {
    position: absolute; left: 86px; top: 1150px; width: 1060px;
    display: grid; grid-template-columns: 306px 382px 360px; row-gap: 38px;
    list-style: none;
  }
  .course-item {
    display: flex; align-items: center; gap: 16px;
    font-weight: 600; font-size: 28px; line-height: 31px; color: var(--cream);
  }
  .course-icon { flex: 0 0 56px; width: 56px; height: 56px; }

  .coupon {
    position: absolute; left: 688px; top: 1372px; width: 400px;
    text-align: center; color: #3b2a12;
  }
  .coupon-intro { font-size: 23px; line-height: 30px; }
  .coupon-code { font-size: 27px; line-height: 32px; color: var(--red); font-weight: 600; }
  .coupon-text {
    font-size: 22px; line-height: 30px; display: inline-block;
    border-bottom: 1.5px solid #6b4a1a; padding: 0 6px 2px;
  }
  .coupon-note { font-size: 15px; line-height: 28px; margin-top: 4px; }

  .guarantee { position: absolute; left: 86px; top: 1492px; }
  .guarantee-label { font-weight: 700; font-size: 28px; color: var(--red); }
  .media-brand { display: flex; align-items: center; gap: 12px; margin-top: 14px; }
  .media-dot { width: 34px; height: 34px; border-radius: 50%; background: #8cbf3a; }
  .media-name { font-weight: 400; font-size: 52px; color: var(--grey-text); line-height: 1; }

  .website {
    position: absolute; right: 84px; top: 1560px;
    font-weight: 400; font-size: 38px; color: var(--orange);
  }
</style>
</head>
<body>
  <main class="ad">
    <div class="photo-area" role="img" aria-label="Foto: donna che annusa un bicchiere di birra ambrata per la degustazione"></div>

    <svg class="ad-shapes" width="1200" height="1697" viewBox="0 0 1200 1697" aria-hidden="true">
      <defs>
        <linearGradient id="orangeBand" x1="0" x2="1" y1="0" y2="0">
          <stop offset="0" stop-color="#f9a51b"/>
          <stop offset="1" stop-color="#f06a1c"/>
        </linearGradient>
        <linearGradient id="redField" x1="0" x2="1" y1="0" y2="1">
          <stop offset="0" stop-color="#d52a1b"/>
          <stop offset="0.6" stop-color="#e63e1f"/>
          <stop offset="1" stop-color="#ee5a22"/>
        </linearGradient>
        <linearGradient id="couponBand" x1="0" x2="1" y1="0" y2="0">
          <stop offset="0" stop-color="#f29a1a"/>
          <stop offset="0.5" stop-color="#f7b92a"/>
          <stop offset="1" stop-color="#fde6b0"/>
        </linearGradient>
      </defs>
      <path d="M0,695 C260,640 520,700 760,830 C900,845 1080,780 1200,700 L1200,1697 L0,1697Z" fill="var(--white)"/>
      <path d="M0,712 C260,672 520,722 760,850 C900,860 1080,795 1200,716 L1200,1697 L0,1697Z" fill="url(#orangeBand)"/>
      <path d="M0,742 C260,720 520,790 760,880 C900,880 1080,810 1200,740 L1200,1697 L0,1697Z" fill="url(#redField)"/>
      <path d="M0,1470 C200,1400 420,1380 620,1375 C820,1370 1000,1350 1200,1330 L1200,1697 L0,1697Z" fill="url(#couponBand)"/>
      <path d="M0,1488 C250,1420 480,1468 680,1512 C850,1548 1050,1505 1200,1428 L1200,1697 L0,1697Z" fill="var(--white)"/>
      <circle cx="917" cy="896" r="196" fill="var(--orange)"/>
      <circle cx="917" cy="896" r="184" fill="var(--white)"/>
      <path d="M757,960 A172,172 0 0 1 850,737" fill="none" stroke="var(--red)" stroke-width="3"/>
      <path d="M1075,830 A172,172 0 0 1 917,1068" fill="none" stroke="var(--red)" stroke-width="3"/>
    </svg>

    <div class="brand">
      <span class="brand-square"></span>
      <span class="brand-name">Bottega Malto</span>
    </div>

    <h1 class="headline">
      <span class="headline-line"><span class="headline-strong red">Corsi</span><span class="headline-light">Online</span></span>
      <span class="headline-line"><span class="headline-light">Sulla</span><span class="headline-strong gold">Birra</span></span>
    </h1>

    <div class="tagline-badge">
      <span><span class="light">Con le </span><span class="gold">birre</span></span>
      <span class="gold">in assaggio</span>
      <span class="grey">spedite</span>
      <span class="red">direttamente</span>
      <span class="red">a casa</span>
    </div>

    <h2 class="offer-title">La proposta<br>didattica di<br>Bottega malto:</h2>

    <ul class="course-list">
      <li class="course-item">
        <svg class="course-icon" viewBox="0 0 56 56"><circle cx="28" cy="28" r="26" fill="var(--gold)" stroke="var(--white)" stroke-width="3"/><path d="M20,16 h14 l-2,24 h-10z" fill="none" stroke="#6b3a10" stroke-width="2.5"/></svg>
        <span>Corso di<br>degustazione</span>
      </li>
      <li class="course-item">
        <svg class="course-icon" viewBox="0 0 56 56"><circle cx="28" cy="28" r="26" fill="var(--gold)" stroke="var(--white)" stroke-width="3"/><rect x="19" y="17" width="14" height="22" rx="2" fill="none" stroke="#6b3a10" stroke-width="2.5"/><path d="M33,22 h4 v10 h-4" fill="none" stroke="#6b3a10" stroke-width="2.5"/></svg>
        <span>Master sulle<br>birre luppolate</span>
      </li>
      <li class="course-item">
        <svg class="course-icon" viewBox="0 0 56 56"><circle cx="28" cy="28" r="26" fill="var(--gold)" stroke="var(--white)" stroke-width="3"/><circle cx="23" cy="25" r="7" fill="none" stroke="#6b3a10" stroke-width="2.5"/><circle cx="33" cy="32" r="7" fill="none" stroke="#6b3a10" stroke-width="2.5"/></svg>
        <span>Master sugli<br>abbinamenti</span>
      </li>
      <li class="course-item">
        <svg class="course-icon" viewBox="0 0 56 56"><circle cx="28" cy="28" r="26" fill="var(--gold)" stroke="var(--white)" stroke-width="3"/><path d="M18,38 L38,18 M24,26 l6,6 M28,22 l6,6" fill="none" stroke="#6b3a10" stroke-width="2.5"/></svg>
        <span>Master sulle<br>birre acide</span>
      </li>
      <li class="course-item">
        <svg class="course-icon" viewBox="0 0 56 56"><circle cx="28" cy="28" r="26" fill="var(--gold)" stroke="var(--white)" stroke-width="3"/><rect x="17" y="19" width="22" height="19" rx="2" fill="none" stroke="#6b3a10" stroke-width="2.5"/><path d="M17,25 h22 M22,15 v6 M34,15 v6" stroke="#6b3a10" stroke-width="2.5"/></svg>
        <span>Focus mensili sul<br>movimento italiano</span>
      </li>
      <li class="course-item">
        <svg class="course-icon" viewBox="0 0 56 56"><circle cx="28" cy="28" r="26" fill="var(--gold)" stroke="var(--white)" stroke-width="3"/><path d="M18,20 h8 v18 h-8z M30,20 h8 v18 h-8z" fill="none" stroke="#6b3a10" stroke-width="2.5"/></svg>
        <span>Esercitazioni<br>pratiche di assaggio</span>
      </li>
    </ul>

    <div class="coupon">
      <p class="coupon-intro">Usa il coupon</p>
      <p class="coupon-code">VELANTRA10</p>
      <p class="coupon-text">per uno sconto di <strong>€ 10</strong> sul carrello*</p>
      <p class="coupon-note">* Coupon valido per tutto il 2022</p>
    </div>

    <div class="guarantee">
      <p class="guarantee-label">Una garanzia</p>
      <div class="media-brand">
        <span class="media-dot"></span>
        <span class="media-name">Diario del Calice</span>
      </div>
    </div>

    <p class="website">www.bottegamalto.it</p>
  </main>
</body>
</html>
```